We need a new e-commerce website. Designed and fully functional.

We are looking for someone who can re-create our website from A-Z and it is fully functional (turnkey). Currently we have a website that we do not like because it is too dark and not easy to use. We would like a more modern, minimalist, elegant, bright and very easy to use. We are also looking for a person who would agree to accompany us in the catalog (with payment in addition to race). To be defined later. We are a designer company, sold through the online store. The jewels are long necklaces with thematic pendants associated with semi-precious stones. 6 themes of pendants, 2 colors and 6 types of semi-precious stones that are combined according to desires. 72 possibilities of combinations. We already have all the connections, texts, payment possibilities, pictures that we all put at your disposal. You can have a look on our website on veltomira.com. We also have a little guide (attached) of what we are looking for this new website. The site must be in 2 languages (French-English) and 3 currencies (dollar, euro and Swiss francs). The shipping costs must be displayed according to the country of destination (KRX) in the shopping cart and for Switzerland the VAT must be displayed directly too. Name of the website: vélta mira jewelry (www.veltomira.com) E-Mail address for the website: info@veltomira.com This website must contain: Home: home page. Welcome page Shop: All articles About: About the creator Contact: e-mail and company contact Press: all the publications in the magazines FAQ & HELP: the company information, orders ... Account: the clients can create an account if they want Purchasing Pannier Languages: English-French Currencies: Dollar, Euro, Swiss Francs

Industry/Entity Type

Jewelry Store

Coding

Coded - Design and coding required

Font styles to use
Sans Serif

Colors

Designer to choose colors to be used in the design.

Requirements
Must have
• This website must be easy to use, modern, elegant and sober.

```html
<!DOCTYPE html>
<html lang="en">
<head>
<meta charset="utf-8">
<title>Vélta Mira Jewelry</title>
<link rel="stylesheet" href="https://fonts.googleapis.com/css2?family=Lora:ital,wght@0,400;0,500;1,400&family=Open+Sans:wght@400;600&display=swap">
<style>
:root{
  --gold:#c8901f;
  --gold-dark:#b07a12;
  --ink:#2b2b2b;
  --muted:#555;
  --line:#e3e3e3;
  --night:#0c0f16;
  --soft:#f4f4f4;
  --white:#fff;
}
*{box-sizing:border-box;margin:0;padding:0}
html,body{width:1200px;height:3125px;overflow:hidden}
body{position:relative;background:var(--white);color:var(--ink);font-family:"Lora",Georgia,serif}
.abs{position:absolute}

/* brand block */
.brand{position:absolute;text-align:center;color:var(--ink);white-space:nowrap}
.brand-name{font-family:"Lora",serif;font-size:40px;letter-spacing:1px;line-height:1;white-space:nowrap}
.brand-sub{font-family:"Lora",serif;font-size:11px;letter-spacing:20px;margin-top:6px;padding-left:20px;line-height:1;white-space:nowrap}
.brand-mark{width:34px;height:34px;border:2px solid var(--ink);border-radius:50%;margin:0 auto 6px}

/* header */
.site-header{position:absolute;left:0;top:0;width:1200px;height:130px}
.header-brand{left:460px;top:12px;width:280px}
.header-brand .brand-name{font-size:36px}
.main-nav a{position:absolute;top:82px;font-size:14px;color:#333;text-decoration:none;letter-spacing:.5px;white-space:nowrap}
.prefs{position:absolute;left:880px;top:18px;font-family:"Open Sans",sans-serif;font-size:13px;line-height:24px;color:#333;white-space:nowrap}
.prefs span{color:var(--gold)}
.flag{display:inline-block;width:14px;height:10px;background:linear-gradient(90deg,#1b3fa0 33%,#fff 33% 66%,#d32 66%);vertical-align:middle}
.cart-icon{position:absolute;left:1020px;top:18px}

/* hero */
.hero{position:absolute;left:0;top:130px;width:1200px;height:516px;background:var(--night)}
.hero-photo{position:absolute;left:0;top:0;width:780px;height:516px;background:linear-gradient(90deg,#3a2a24 0%,#8a6252 40%,#3c2c28 75%,var(--night) 100%)}
.play{position:absolute;left:362px;top:230px}
.hero-brand{position:absolute;left:620px;top:168px;width:500px;text-align:center;color:var(--gold)}
.hero-brand .brand-name{font-size:64px;letter-spacing:1px}
.hero-brand .brand-sub{font-size:17px;letter-spacing:24px;padding-left:24px;margin-top:12px;color:var(--gold)}
.hero-tag{position:absolute;left:620px;top:286px;width:500px;text-align:center;color:#fff;font-size:18px;letter-spacing:.5px;white-space:nowrap}

/* collections */
.tile{position:absolute}
.tile-label{position:absolute;left:50px;right:50px;bottom:26px;height:52px;background:rgba(255,255,255,.82);border:1px dashed #999;outline:4px solid rgba(255,255,255,.82);display:flex;align-items:center;justify-content:center;font-size:22px;color:#222}
.tile-feature{position:absolute;left:8px;right:8px;bottom:0;height:114px;background:rgba(200,135,15,.88);color:#fff;text-align:center}
.tile-feature h3{font-weight:400;font-size:32px;margin-top:14px}
.tile-feature p{font-style:italic;font-size:20px;margin-top:4px}

/* featured */
.section-title{position:absolute;left:0;width:1200px;text-align:center;font-size:26px;font-weight:400;letter-spacing:.5px;color:#222}
.title-rule{position:absolute;left:565px;width:70px;height:2px;background:var(--gold)}
.product{position:absolute;top:1487px;width:233px;height:356px;border:1px solid var(--line);background:#fff;text-align:center}
.product-img{height:254px;background:linear-gradient(180deg,#eeeeee,#f6f6f6)}
.stars{color:var(--gold-dark);font-size:13px;letter-spacing:2px;margin-top:12px}
.product h4{font-weight:400;font-size:20px;margin-top:6px}
.price{color:var(--gold);font-size:17px;margin-top:6px}
.quick{position:absolute;left:200px;width:26px;height:26px;background:#fff;border:1px solid #ddd;display:flex;align-items:center;justify-content:center}

/* reviews */
.reviews{position:absolute;left:0;top:1900px;width:1200px;height:433px;background:var(--soft)}
.avatar{position:absolute;left:548px;top:110px;width:104px;height:104px;border-radius:50%;border:4px solid #fff;box-shadow:0 0 0 1px #ccc;background:radial-gradient(circle,#4d8e8a,#2b3c44)}
.quote{position:absolute;left:250px;top:225px;width:700px;text-align:center;font-style:italic;font-size:13.5px;line-height:32px;color:#555}
.qmark{color:#bbb;font-size:34px;font-style:normal;line-height:0}
.reviewer{position:absolute;left:0;width:1200px;top:350px;text-align:center;color:var(--gold);font-size:18px}
.posted{position:absolute;left:0;width:1200px;top:378px;text-align:center;font-family:"Open Sans",sans-serif;font-size:12px;color:#555}

/* promo */
.promo{position:absolute;left:0;top:2333px;width:1200px;height:429px;background:linear-gradient(90deg,#c1a287 0%,#d8c0a8 45%,#e4d3c0 100%)}
.promo-photo{position:absolute;left:720px;top:0;width:400px;height:429px;background:linear-gradient(90deg,rgba(90,62,48,0) 0%,#6a4c3e 40%,#3e2c26 70%,rgba(200,175,150,0) 100%)}
.promo h2{position:absolute;left:158px;top:112px;color:#fff;font-weight:400;font-size:30px;line-height:44px;white-space:nowrap}
.promo h2 small{display:block;font-size:36px}
.promo p{position:absolute;left:158px;top:216px;width:460px;color:#fff;font-style:italic;font-size:14.5px;line-height:31px}

/* footer */
.footer-brand{left:112px;top:2795px;width:196px}
.footer-brand .brand-mark{width:30px;height:30px;margin-bottom:8px}
.footer-brand .brand-name{font-size:31px;letter-spacing:0}
.footer-brand .brand-sub{font-size:10px;letter-spacing:16px;padding-left:16px;margin-top:7px}
.footer-about{position:absolute;left:112px;top:2914px;width:240px;font-family:"Open Sans",sans-serif;font-size:12px;line-height:25px;color:#333}
.footer-col h5{position:absolute;top:2830px;font-weight:400;font-size:16px;letter-spacing:.5px;color:#222;white-space:nowrap}
.footer-list{position:absolute;top:2870px;list-style:none;font-family:"Open Sans",sans-serif;font-size:12px;color:#333}
.footer-list li{height:25.6px;padding-left:28px;position:relative;white-space:nowrap}
.footer-list li::before{content:"";position:absolute;left:0;top:5px;border-left:5px solid #333;border-top:4px solid transparent;border-bottom:4px solid transparent}
.contact-list{position:absolute;left:881px;top:2875px;list-style:none;font-family:"Open Sans",sans-serif;font-size:12px;color:#333}
.contact-list li{display:flex;gap:14px;min-height:28px}
.contact-list svg{flex:none;margin-top:1px}
.contact-list a{color:#333}
.footer-rule{position:absolute;left:112px;top:3056px;width:975px;height:1px;background:#ccc}
.copyright{position:absolute;left:112px;top:3086px;font-family:"Open Sans",sans-serif;font-size:12px;color:#333;white-space:nowrap}
.cards{position:absolute;left:932px;top:3082px;display:flex;gap:4px}
.cards span{width:38px;height:22px;border-radius:3px}
</style>
</head>
<body>

<header class="site-header">
  <nav class="main-nav">
    <a style="left:140px">HOME</a>
    <a style="left:255px">ABOUT US</a>
    <a style="left:395px">SHOP</a>
    <a style="left:740px">CONTACT</a>
    <a style="left:877px">PRESS</a>
    <a style="left:990px">FAQ &amp; HELP</a>
  </nav>
  <div class="brand header-brand">
    <div class="brand-mark"></div>
    <div class="brand-name">VÉLTA MIRA</div>
    <div class="brand-sub">JEWELRY</div>
  </div>
  <div class="prefs">
    Langues : <i class="flag"></i> <span>FR-AN</span><br>
    Devise : <span>Euro-Dollar</span>
  </div>
  <svg class="cart-icon" width="44" height="36" viewBox="0 0 44 36" fill="none" stroke="#c8901f" stroke-width="2.5">
    <path d="M2 4h7l5 20h22l5-14H12"/><circle cx="17" cy="31" r="3"/><circle cx="33" cy="31" r="3"/>
  </svg>
</header>

<section class="hero">
  <div class="hero-photo" role="img" aria-label="Portrait of a model wearing a long necklace with a themed pendant"></div>
  <svg class="play" width="90" height="90" viewBox="0 0 90 90">
    <circle cx="45" cy="45" r="41" fill="none" stroke="#fff" stroke-width="4"/>
    <path d="M36 28v34l28-17z" fill="#fff"/>
  </svg>
  <div class="hero-brand">
    <div class="brand-name">VÉLTA MIRA</div>
    <div class="brand-sub">JEWELRY</div>
  </div>
  <div class="hero-tag">ELEGANCE BY NATURE</div>
</section>

<section class="collections">
  <div class="tile" style="left:112px;top:692px;width:313px;height:320px;background:linear-gradient(160deg,#a98e7c,#6e5244 60%,#ddd0cb)" role="img" aria-label="Model wearing the Bee pendant">
    <div class="tile-label">Bee</div>
  </div>
  <div class="tile" style="left:112px;top:1029px;width:313px;height:321px;background:linear-gradient(150deg,#9c3a32,#d77a60 50%,#7d2a2a)" role="img" aria-label="Model wearing the Ladybird pendant">
    <div class="tile-label">Ladybird</div>
  </div>
  <div class="tile" style="left:437px;top:692px;width:323px;height:412px;background:linear-gradient(160deg,#1f6f78,#8d5d48 50%,#2a5e66)" role="img" aria-label="Model holding the Dragon pendant">
    <div class="tile-feature"><h3>Dragon</h3><p>The pendant of Protection</p></div>
  </div>
  <div class="tile" style="left:437px;top:1117px;width:323px;height:233px;background:linear-gradient(180deg,#4a4a4e,#7a675c 55%,#cfd6d4)" role="img" aria-label="Model wearing the Toucan pendant">
    <div class="tile-label">Toucan</div>
  </div>
  <div class="tile" style="left:773px;top:692px;width:314px;height:320px;background:linear-gradient(160deg,#4a1630,#b06a58 50%,#2a0c1c)" role="img" aria-label="Model wearing the Frog pendant">
    <div class="tile-label">Frog</div>
  </div>
  <div class="tile" style="left:773px;top:1029px;width:314px;height:321px;background:linear-gradient(160deg,#7fc6c8,#5a4538 50%,#9fd6d6)" role="img" aria-label="Model wearing the Dragonfly pendant">
    <div class="tile-label">Dragonfly</div>
  </div>
</section>

<section class="featured">
  <h2 class="section-title" style="top:1408px">FEATURED PRODUCTS</h2>
  <div class="title-rule" style="top:1452px"></div>

  <article class="product" style="left:112px">
    <div class="product-img" role="img" aria-label="Bee pendant on a gold chain"></div>
    <div class="stars">★★★★★</div><h4>BEE</h4><div class="price">$290.00</div>
    <span class="quick" style="top:140px"><svg width="12" height="12" viewBox="0 0 24 24"><path d="M12 21 3 12a5 5 0 0 1 9-6 5 5 0 0 1 9 6z" fill="#333"/></svg></span>
    <span class="quick" style="top:172px"><svg width="14" height="12" viewBox="0 0 24 16"><path d="M1 8s4-7 11-7 11 7 11 7-4 7-11 7S1 8 1 8z" fill="none" stroke="#333" stroke-width="2"/><circle cx="12" cy="8" r="3" fill="#333"/></svg></span>
    <span class="quick" style="top:204px"><svg width="13" height="12" viewBox="0 0 24 22"><path d="M1 2h4l3 12h12l3-9H6" fill="none" stroke="#333" stroke-width="2.4"/><circle cx="9" cy="19" r="2" fill="#333"/><circle cx="18" cy="19" r="2" fill="#333"/></svg></span>
  </article>
  <article class="product" style="left:360px">
    <div class="product-img" role="img" aria-label="Dragon pendant on a violet stone chain"></div>
    <div class="stars">★★★★★</div><h4>DRAGON</h4><div class="price">$290.00</div>
  </article>
  <article class="product" style="left:606px">
    <div class="product-img" role="img" aria-label="Dragonfly pendant on a grey stone chain"></div>
    <div class="stars">★★★★★</div><h4>DRAGONFLY</h4><div class="price">$290.00</div>
  </article>
  <article class="product" style="left:854px">
    <div class="product-img" role="img" aria-label="Frog pendant on a green stone chain"></div>
    <div class="stars">★★★★★</div><h4>FROG</h4><div class="price">$290.00</div>
  </article>
</section>

<section class="reviews">
  <h2 class="section-title" style="top:32px">CLIENT REVIEWS</h2>
  <div class="title-rule" style="top:75px"></div>
  <div class="avatar" role="img" aria-label="Client portrait"></div>
  <p class="quote"><span class="qmark">“ </span>Sed ut perspiciatis unde omnis iste natus error sit voluptatem accusantium doloremque laudantium, totam rem aperiam, eaque ipsa quae ab illo inventore veritatis et quasi architecto beatae vitae dicta sunt explicabo. Nemo enim quia consequuntur magni dolores eos qui ratione voluptatem sequi nesciunt.<span class="qmark"> ”</span></p>
  <div class="reviewer">Mara Ellison</div>
  <div class="posted">Posed on 08 Feb 2019</div>
</section>

<section class="promo">
  <div class="promo-photo" role="img" aria-label="Model in a white dress wearing a long necklace"></div>
  <h2>MY CREATIONS,<small>A Homage To Mother Earth</small></h2>
  <p>These Themed Pendants Can Be Mixed And Matched With Interchangeable Fine Gemstones Thanks To Snap Rings. Match Your Favourite Pendant With A Gorgeous Gemstone Of Your Choice. Vibrant Colours And Infinite Possibilities...</p>
</section>

<footer>
  <div class="brand abs footer-brand">
    <div class="brand-mark"></div>
    <div class="brand-name">VÉLTA MIRA</div>
    <div class="brand-sub">JEWELRY</div>
  </div>
  <p class="footer-about">Sed ut perspiciatis unde omnis iste natus error sit voluptatem accusantium dolorem que laudantium, totam rem aperiam, eaque vitae dicta sunt explicabo.</p>

  <div class="footer-col"><h5 style="left:427px">CUSTOMER SERVICE</h5></div>
  <ul class="footer-list" style="left:427px">
    <li>Home</li><li>About</li><li>Collection</li><li>Contact</li><li>Faq &amp; Help</li><li>Account</li>
  </ul>
  <div class="footer-col"><h5 style="left:673px">MY ACCOUNT</h5></div>
  <ul class="footer-list" style="left:673px">
    <li>My account</li><li>Orders</li><li>Addresses</li><li>Shopping cart</li><li>Wishlist</li>
  </ul>
  <div class="footer-col"><h5 style="left:881px">CONTACT US</h5></div>
  <ul class="contact-list">
    <li><svg width="14" height="14" viewBox="0 0 24 24"><path d="M6 2h4l2 5-3 2a12 12 0 0 0 6 6l2-3 5 2v4a2 2 0 0 1-2 2A19 19 0 0 1 4 4a2 2 0 0 1 2-2z" fill="#333"/></svg>(000)-484-2290 (Phone)</li>
    <li><svg width="14" height="14" viewBox="0 0 24 24"><rect x="3" y="8" width="18" height="10" rx="2" fill="#333"/><rect x="7" y="3" width="10" height="5" fill="#333"/></svg>(000)-484-2290 &nbsp;(Fax)</li>
    <li><svg width="14" height="14" viewBox="0 0 24 24"><rect x="2" y="5" width="20" height="14" fill="#333"/><path d="M2 5l10 8 10-8" stroke="#fff" stroke-width="1.5" fill="none"/></svg><a>info@veltomira.com/</a></li>
    <li><svg width="14" height="14" viewBox="0 0 24 24"><path d="M12 2a7 7 0 0 0-7 7c0 5 7 13 7 13s7-8 7-13a7 7 0 0 0-7-7z" fill="#333"/><circle cx="12" cy="9" r="2.5" fill="#fff"/></svg><span>#1452 Lorem Ipsum Dummy<br>Text Lorem Ipsum</span></li>
  </ul>

  <div class="footer-rule"></div>
  <div class="copyright">© Copyright 2019 Vélta Mira.All Rights Reserved</div>
  <div class="cards" aria-label="Accepted payment cards">
    <span style="background:#2a4c9a"></span>
    <span style="background:#e8a13a"></span>
    <span style="background:#3a8fd0"></span>
    <span style="background:#d9d9d9"></span>
  </div>
</footer>

</body>
</html>
```